Local Directory Ad

We currently have an advertisement in our local directory (see attached). We would like to make it look more appealing.
Dimensions are 110mm H X 175mm W
We would like to keep the same colours and contact details remain the same.
Most of the content can remain the same, Just remove the line Tax effective remote area salary packaging and add in Self Managed Super Funds.We want to change mortgage broking to Mortgage Broking and Loan Structuring.

We want to change the line Local accountants Local Knowledge Local Experience - to something like Local Expertise You Can Trust or unsurpassed local knowledge but open to suggestions on this.

there are some good designs posted so far. I particulalry like the ones from pulmawick, korbu41, and the last one posted by wexlorunti and PLV. Keep up the good work guys

```html
<!DOCTYPE html>
<html lang="en">
<head>
<meta charset="utf-8">
<title>Tarrow Accounting &amp; Finance – Directory Ad</title>
<link rel="stylesheet" href="https://fonts.googleapis.com/css2?family=Open+Sans:wght@300;400&family=Archivo+Black&family=Rubik:wght@700&family=Questrial&family=Exo+2:wght@600;700&display=swap">
<style>
  :root {
    --backdrop: #9b9b9b;
    --slate: #3c4a47;
    --brand-red: #cc2229;
    --paper: #ffffff;
    --ink: #111111;
  }
  * { box-sizing: border-box; margin: 0; padding: 0; }
  html, body { width: 1200px; height: 792px; overflow: hidden; }
  body { background: var(--backdrop); position: relative; font-family: "Questrial", sans-serif; }

  .ad { position: absolute; left: 80px; top: 69px; width: 1040px; height: 653px; background: var(--paper); overflow: hidden; }
  .ad__header { position: absolute; left: 0; top: 0; width: 100%; height: 279px; background: var(--slate); }
  .ad__footer-band { position: absolute; left: 0; bottom: 0; width: 100%; height: 17px; background: var(--slate); }

  .wordmark { position: absolute; left: 0; top: 44px; width: 100%; text-align: center; color: var(--paper); font-family: "Open Sans", sans-serif; font-weight: 300; }
  .wordmark__name { display: block; font-size: 70px; letter-spacing: 16px; line-height: 1; padding-left: 16px; }
  .wordmark__sub { display: block; margin-top: 8px; font-size: 38px; letter-spacing: 9px; line-height: 1; padding-left: 9px; }
  .licence { position: absolute; left: 0; top: 162px; width: 100%; text-align: center; color: var(--paper); font-family: "Open Sans", sans-serif; font-size: 17px; letter-spacing: 3px; }

  .slogan { position: absolute; left: 120px; top: 209px; width: 800px; height: 134px; background: var(--brand-red); border: 6px solid var(--paper); border-radius: 12px; }
  .slogan__icon { position: absolute; left: 30px; top: 14px; width: 118px; height: 96px; background: var(--paper); border-radius: 6px; }
  .slogan__text { position: absolute; left: 184px; top: 18px; width: 590px; text-align: center; color: var(--paper); font-family: "Archivo Black", sans-serif; font-size: 40px; line-height: 42px; letter-spacing: 2px; text-transform: uppercase; }

  .services { position: absolute; left: 0; top: 364px; width: 100%; text-align: center; }
  .services__lead { color: var(--brand-red); font-family: "Rubik", sans-serif; font-weight: 700; font-size: 33px; letter-spacing: 0.5px; line-height: 1; }
  .services__list { margin-top: 12px; list-style: none; color: var(--ink); font-size: 26px; line-height: 33px; }

  .contact { position: absolute; top: 527px; width: 520px; text-align: center; color: var(--ink); font-family: "Exo 2", sans-serif; font-weight: 600; font-size: 27px; line-height: 30px; letter-spacing: 0.8px; font-style: normal; }
  .contact--address { left: 0; }
  .contact--reach { left: 520px; }
  .contact__web { color: var(--brand-red); font-weight: 700; font-size: 26px; letter-spacing: 2px; }
  .divider { position: absolute; left: 513px; top: 536px; width: 6px; height: 100px; background: var(--slate); }
</style>
</head>
<body>
  <main class="ad">
    <header class="ad__header">
      <h1 class="wordmark">
        <span class="wordmark__name">TARROW</span>
        <span class="wordmark__sub">ACCOUNTING &amp; FINANCE</span>
      </h1>
      <p class="licence">AUSTRALIAN CREDIT LICENCE 412 908</p>
    </header>

    <section class="slogan">
      <div class="slogan__icon" role="img" aria-label="Illustration of a stack of books wearing glasses"></div>
      <p class="slogan__text">Local Expertise<br>You Can Trust</p>
    </section>

    <section class="services">
      <h2 class="services__lead">We are here for you all year round to assist with...</h2>
      <ul class="services__list">
        <li>•Accounting &amp; Taxation •Business Advice •GST and BAS’s</li>
        <li>•Mortgage Broking and Loan Structuring •Bookkeeping</li>
        <li>•Self Managed Super Funds for your employees</li>
      </ul>
    </section>

    <address class="contact contact--address">
      Shop 5, Marlin Arcade<br>
      12 Keel St. Port Tarrow<br>
      PO Box 418, Port Tarrow 6799
    </address>
    <div class="divider"></div>
    <address class="contact contact--reach">
      reception@tarrowaf.com.au<br>
      Ph: 9100 4821 Fax: 9100 4822<br>
      <span class="contact__web">www.tarrowaf.com.au</span>
    </address>

    <div class="ad__footer-band"></div>
  </main>
</body>
</html>
```